Orbix Pellumo Relay Monitor Interface

We have a live help chat software that we need a new chat monitor interface designed for. Something that will be easy to make responsive. I will provide screen shots of the current interface and a picture of the new admin back-end that we want it to look similar too. This project should be fairly straight forward and easy. See below.

Important Notes:

1. You DO NOT need to worry about the actual list of visitors on the site in the middle as that will be handled by the grid system we use.

2. We have decided to eliminate the logo from the monitor all together to make it more compact. Just the words "Orbix Pellumo" and a copyright notice will be enough.

3. We want the chat monitor interface to utilize the same colors and look as the new admin interface if possible. See attached "new_admin_interface.png" image.

4. Although I want to utilize the same colors as the admin area, it should NOT utilize the same header and footer as the admin area. I only referenced the admin area so that you can get color ideas from it. Consider it a popup window and assume the same amount of space will be used. Although it will have the ability to be resized we must not waste space.

Target Market(s)

N/A

Industry/Entity Type

Software

Number of Pages Required

1 page

Requirements
Must have
• See Description.
Nice to have
• See Description.
Should not have
• See Description.

```html
<!DOCTYPE html>
<html lang="en">
<head>
<meta charset="utf-8">
<title>Orbix Pellumo Relay – Chat Monitor</title>
<link href="https://fonts.googleapis.com/css2?family=Open+Sans:wght@400;600;700&family=Roboto:wght@400;500&display=swap" rel="stylesheet">
<style>
:root{
  --page-bg:#2b3744;
  --page-panel:#2f3b48;
  --page-line:#3a4654;
  --page-text:#56636f;
  --page-text-strong:#6b7784;
  --header-bg:#1e2a36;
  --nav-bg:#1a2530;
  --modal-bg:#e9e9e9;
  --panel-bg:#ffffff;
  --panel-head:#f3f3f3;
  --border:#d0d0d0;
  --table-head:#2d3e50;
  --table-head-2:#1f2d3b;
  --row-alt:#eef2f6;
  --ink:#2a2f35;
  --ink-soft:#444;
  --brand-dark:#1f3a4f;
  --online:#7cbd1e;
  --offline:#8a8a8a;
  --icon-grey:#b9bdc1;
  --icon-orange:#f0a020;
  --icon-blue:#1e8fd9;
}
*{box-sizing:border-box;margin:0;padding:0}
html,body{width:1072px;height:1200px;overflow:hidden}
body{position:relative;background:var(--page-bg);font-family:"Open Sans",Arial,sans-serif;color:var(--ink)}
.abs{position:absolute}

/* ---------- admin backdrop ---------- */
.admin-header{left:24px;top:0;width:1024px;height:126px;background:var(--header-bg)}
.admin-brand{left:46px;top:52px;font-size:17px;font-weight:700;color:#3c4a57}
.admin-welcome{right:46px;top:12px;text-align:right;font-size:12px;color:#55616d;line-height:20px}
.admin-welcome b{font-size:13px;color:#5e6a76}
.admin-nav{left:24px;top:86px;width:1024px;height:38px;background:var(--nav-bg);display:flex;align-items:center;padding-left:14px;gap:28px;font-size:12px;font-weight:600;color:#4e5a66}
.admin-nav .home{width:28px;height:26px;background:#25313d}
.bg-panel{background:var(--page-panel);border:1px solid var(--page-line)}
.bg-title{font-size:12px;color:var(--page-text);padding:10px 12px;border-bottom:1px solid var(--page-line)}
.bg-label{font-size:11px;color:var(--page-text-strong);font-weight:700}
.bg-news{font-size:10.5px;line-height:17px;color:#4f5c68}
.bg-news h4{font-size:12.5px;color:#5d6975;margin-bottom:2px}
.admin-footer{left:24px;top:1158px;font-size:10px;color:#4a5662}

/* ---------- monitor popup ---------- */
.monitor{left:107px;top:287px;width:861px;height:633px;background:var(--modal-bg);box-shadow:0 0 30px rgba(0,0,0,.35)}
.close-btn{left:931px;top:278px;width:46px;height:46px;border-radius:50%;background:#fff;box-shadow:0 1px 4px rgba(0,0,0,.3)}
.wordmark{left:134px;top:312px;font-size:21px;font-weight:700;letter-spacing:.5px;color:var(--brand-dark)}

.panel{background:var(--panel-bg);border:1px solid var(--border)}
.panel-head{height:36px;background:var(--panel-head);border-bottom:1px solid var(--border);display:flex;align-items:center;gap:8px;padding-left:13px;font-size:12.5px;color:var(--ink)}
.panel-head.lg{height:37px;font-size:13.5px}

.visitors{left:134px;top:357px;width:807px;height:225px}
.visitor-table{position:absolute;left:0;top:36px;width:794px;border-collapse:collapse;font-family:"Roboto",Arial,sans-serif;table-layout:fixed}
.visitor-table th{height:35px;background:linear-gradient(var(--table-head),var(--table-head-2));color:#fff;font-size:12.5px;font-weight:500;text-align:left;padding-left:10px;border-right:1px solid #3d5064}
.visitor-table td{height:30.5px;font-size:11px;color:var(--ink-soft);padding-left:10px;border-right:1px solid #dde2e7;border-bottom:1px solid #e2e6ea;white-space:nowrap;overflow:hidden}
.visitor-table tr:nth-child(even) td{background:var(--row-alt)}
.visitor-table td.loc{text-overflow:ellipsis}
.visitor-table td.ico{text-align:center;padding-left:0}
.scrollbar{position:absolute;right:0;width:13px;background:#f4f4f4;border-left:1px solid #ddd}
.scrollbar .thumb{position:absolute;left:1px;width:10px;background:#e2e2e2;border:1px solid #aaa;border-radius:2px}
.scrollbar .arrow{position:absolute;left:1px;width:10px;height:10px;border:1px solid #999;background:#eee}

.monitor-info{left:134px;top:610px;width:557px;height:284px}
.tabs{position:absolute;left:0;top:37px;width:555px;height:42px;background:#eaeaea;border-bottom:1px solid var(--border);display:flex;font-size:12.5px}
.tab{width:141px;display:flex;align-items:center;justify-content:center;color:var(--ink)}
.tab.active{background:#fff;border:1px solid var(--border);border-bottom:none;height:43px}
.footprints{position:absolute;left:26px;top:104px;width:491px;border-collapse:collapse;font-family:"Roboto",Arial,sans-serif}
.footprints td{height:30.3px;font-size:11.5px;color:var(--ink-soft);padding-left:12px;white-space:nowrap}
.footprints tr:nth-child(odd) td{background:var(--row-alt)}
.footprints td.time{width:66px}

.operators{left:718px;top:610px;width:223px;height:284px}
.op-list{position:absolute;left:18px;top:52px;list-style:none;font-family:"Roboto",Arial,sans-serif;font-size:12.5px}
.op-list li{height:22px;display:flex;align-items:center;gap:9px;color:var(--offline)}
.op-list li::before{content:"";width:6px;height:6px;border-radius:50%;background:var(--offline)}
.op-list li.online{color:var(--ink)}
.op-list li.online::before{background:var(--online)}
</style>
</head>
<body>

<div class="abs admin-header"></div>
<div class="abs admin-brand">Orbix Pellumo</div>
<div class="abs admin-welcome"><b>Welcome back, Admin</b><br>Logged in as admin<br>Logout · Get Support</div>
<nav class="abs admin-nav">
  <span class="home"></span><span>Operators ▾</span><span>Departments ▾</span><span>Transcripts ▾</span><span>Settings ▾</span><span>Reports ▾</span><span>Actions ▾</span>
</nav>

<section class="abs bg-panel" style="left:26px;top:148px;width:322px;height:248px">
  <div class="bg-title">Quick Stats</div>
  <div class="abs bg-panel" style="left:14px;top:48px;width:140px;height:82px;text-align:center;padding-top:26px;font-size:11px;color:var(--page-text)">Operators Online</div>
  <div class="abs bg-panel" style="left:166px;top:48px;width:140px;height:82px;text-align:center;padding-top:26px;font-size:11px;color:var(--page-text)">Current Chats</div>
  <div class="abs" style="left:40px;top:164px;font-size:11px;color:var(--page-text)">Todays</div>
</section>
<section class="abs bg-panel" style="left:26px;top:420px;width:322px;height:230px">
  <div class="bg-title">Shortcuts</div>
  <div class="abs bg-panel" style="left:14px;top:48px;width:100px;height:70px"></div>
  <div class="abs bg-panel" style="left:14px;top:128px;width:100px;height:70px;font-size:10px;color:var(--page-text);padding:50px 0 0 26px">Reports</div>
</section>
<section class="abs bg-panel" style="left:26px;top:660px;width:322px;height:276px">
  <div class="bg-title">License Info</div>
  <div class="abs bg-label" style="left:16px;top:60px;line-height:26px">Registered To<br>Purchase Date<br>License Domain<br><br><br>License Number<br>Software Version<br>Latest Version</div>
</section>

<section class="abs bg-panel" style="left:375px;top:148px;width:673px;height:390px">
  <div class="bg-title">Traffic Stats</div>
  <div class="abs" style="left:56px;top:54px;width:554px;height:300px;border:1px solid #3f4b58"></div>
  <div class="abs" style="left:484px;top:110px;width:40px;height:244px;background:#34404d"></div>
</section>
<section class="abs bg-panel" style="left:375px;top:548px;width:673px;height:530px">
  <div class="abs" style="left:0;top:36px;width:673px;height:32px;background:#223040"></div>
  <div class="abs bg-news" style="left:14px;top:374px;width:640px">
    <p>Orbix Pellumo 3.1 is now in the client area. For details on changes in this release please view the Change Log.</p>
    <h4 style="margin-top:14px">Orbix Pellumo Version 3.0.0 Available</h4>
    <p>Mon, May 16 2011</p>
    <p>We are pleased to share that a new version of Orbix Pellumo is out today. After months of work it is ready to download in the client area. It brings new features, faster loading, and the traffic monitor now supports all current browsers. See the Change Log for the full list of updates.</p>
  </div>
</section>
<div class="abs admin-footer">©Copyright 2001-2016 Kelvane Works, Inc. · Orbix Pellumo 3.1.0</div>

<div class="abs monitor"></div>
<div class="abs close-btn">
  <svg width="46" height="46" viewBox="0 0 46 46"><path d="M16 16L30 30M30 16L16 30" stroke="#1d2a36" stroke-width="4.5" stroke-linecap="round"/></svg>
</div>
<div class="abs wordmark">ORBIX PELLUMO</div>

<section class="abs panel visitors">
  <div class="panel-head">
    <svg width="13" height="11" viewBox="0 0 13 11"><rect y="0" width="13" height="2" fill="#444"/><rect y="4.5" width="13" height="2" fill="#444"/><rect y="9" width="13" height="2" fill="#444"/></svg>
    Operators Online
  </div>
  <table class="visitor-table">
    <colgroup><col style="width:115px"><col style="width:72px"><col style="width:81px"><col style="width:62px"><col style="width:338px"><col style="width:63px"><col style="width:63px"></colgroup>
    <tr><th>IP Address</th><th>Stutus</th><th>Duration</th><th>Pages</th><th>Location</th><th>Brow.</th><th>Os</th></tr>
    <tr><td>75.142.132.122</td><td>In Site</td><td>0:15:14</td><td>1</td><td class="loc">https://learn.huehall.com/blog/100-color-combinati ...</td>
      <td class="ico"><svg width="12" height="12"><circle cx="6" cy="6" r="5.5" fill="var(--icon-grey)"/></svg></td>
      <td class="ico"><svg width="12" height="10"><rect width="12" height="10" fill="var(--icon-grey)"/></svg></td></tr>
    <tr><td>71.140.58.59</td><td>In Site</td><td>0:15:14</td><td>15</td><td class="loc">https://www.sproutvale.se/full/Page/coaching13</td>
      <td class="ico"><svg width="12" height="12"><circle cx="6" cy="6" r="5.5" fill="var(--icon-orange)"/></svg></td>
      <td class="ico"><svg width="12" height="10"><rect width="12" height="10" fill="var(--icon-blue)"/></svg></td></tr>
    <tr><td>199.201.102.196</td><td>In Site</td><td>0:15:14</td><td>1</td><td class="loc">https://tintfall.io/</td>
      <td class="ico"><svg width="12" height="12"><circle cx="6" cy="6" r="5.5" fill="var(--icon-grey)"/></svg></td>
      <td class="ico"><svg width="12" height="10"><rect width="12" height="10" fill="var(--icon-grey)"/></svg></td></tr>
    <tr><td>66.42.219.226</td><td>In Site</td><td>0:15:14</td><td>7</td><td class="loc">https://learn.huehall.com/blog/100-color-combinati ...</td>
      <td class="ico"><svg width="12" height="12"><circle cx="6" cy="6" r="5.5" fill="var(--icon-grey)"/></svg></td>
      <td class="ico"><svg width="12" height="10"><rect width="12" height="10" fill="var(--icon-grey)"/></svg></td></tr>
    <tr><td>75.142.132.122</td><td>In Site</td><td>0:15:14</td><td>1</td><td class="loc">https://learn.huehall.com/blog/100-color-combinati ...</td>
      <td class="ico"><svg width="12" height="12"><circle cx="6" cy="6" r="5.5" fill="var(--icon-grey)"/></svg></td>
      <td class="ico"><svg width="12" height="10"><rect width="12" height="10" fill="var(--icon-grey)"/></svg></td></tr>
  </table>
  <div class="scrollbar" style="top:71px;height:153px">
    <div class="arrow" style="top:2px"></div>
    <div class="thumb" style="top:48px;height:44px"></div>
    <div class="arrow" style="bottom:2px"></div>
  </div>
</section>

<section class="abs panel monitor-info">
  <div class="panel-head lg">
    <svg width="15" height="13" viewBox="0 0 15 13"><rect x="1" y="1" width="13" height="8" fill="none" stroke="#333" stroke-width="2"/><rect x="4" y="11" width="7" height="2" fill="#333"/></svg>
    Monitor Info
  </div>
  <div class="tabs">
    <div class="tab">Visitor Info</div>
    <div class="tab active">Footprints</div>
    <div class="tab">Chat</div>
  </div>
  <table class="footprints">
    <tr><td class="time">0:15:14</td><td>https://learn.huehall.com/blog/100-color-combinations/</td></tr>
    <tr><td class="time">0:15:14</td><td>https://www.sproutvale.se/full/Page/coaching13</td></tr>
    <tr><td class="time">0:15:14</td><td>https://learn.huehall.com/blog/100-color-combinations/</td></tr>
    <tr><td class="time">0:15:14</td><td>https://learn.huehall.com/blog/100-color-combinations/</td></tr>
    <tr><td class="time">0:15:14</td><td>https://www.sproutvale.se/full/Page/coaching13</td></tr>
  </table>
  <div class="scrollbar" style="top:80px;height:202px">
    <div class="arrow" style="top:2px"></div>
    <div class="thumb" style="top:50px;height:48px"></div>
    <div class="arrow" style="bottom:2px"></div>
  </div>
</section>

<section class="abs panel operators">
  <div class="panel-head lg">
    <svg width="15" height="12" viewBox="0 0 15 12"><circle cx="5" cy="3" r="2.6" fill="#555"/><path d="M0 11c0-3 2-5 5-5s5 2 5 5z" fill="#555"/><circle cx="11" cy="3.5" r="2.2" fill="#777"/><path d="M8 11c0-2.6 1.4-4.4 3-4.4s4 1.6 4 4.4z" fill="#777"/></svg>
    Operators
  </div>
  <ul class="op-list">
    <li class="online">Dylan Marsh</li>
    <li class="online">Owen Reyes</li>
    <li>Ramon Ibarra</li>
    <li>Grant Mercer</li>
    <li>Nora</li>
    <li>Kieran Holt</li>
  </ul>
</section>

</body>
</html>
```